Design a Flooring flyer based on out information

We are a flooring company who specialise in supply & installation of high quality flooring (Laminate, SPC vinyl planks and engineered timber)

The colours in flyer should only consist the same colours in business logo as attached

Flyer needs to show customers we offer samples for free delivered to see quality and colours. This can only be ordered via our website.

Contact number: 1300 482 915

www.breltonsflooringsolutions.com.au

instagram: breltonssolutionsgroup

Inregards to texts for flyer.. I will attach our body content of 'about us' Please add some key points in flyer

About Us

Marcus Brelton founded Brelton’s Flooring Solutions with one goal in mind – quality flooring equipment. Our team is made up of flooring professionals who have had extensive experience with flooring installation themselves. Therefore, we are experts at equipping customers with the right products they need to succeed.

The team at Brelton’s Flooring Solutions have had mastered all sorts of flooring technology as we are always focused on innovation and advancement. For example, our expert team has mastered the correct click system that floors need to be suitable for water spills, surface scratches, and foot traffic impact. This is just one of the ways our hands-on team strives to provide our customers with the innovative flooring technology.

Additionally, we make sure that our products are specifically suited to flourish in the Australian environment, and all of our equipment have been approved by Australian standards. Rain, drought or shine, our products are built to survive in Australian weather.

At Brelton’s Flooring Solutions, we work with you to ensure the best outcome for your unique situation. Just contact our friendly and knowledgeable team today to find out more.

Target Market(s)

Home owners

Requirements
Must have
• Logo colours, modern and expensive

```html
<!DOCTYPE html>
<html lang="en">
<head>
<meta charset="utf-8">
<title>Brelton’s Flooring Solutions — Flyer</title>
<link rel="stylesheet" href="https://fonts.googleapis.com/css2?family=Poppins:wght@400;500;600;800&display=swap">
<style>
  :root{
    --green:#86c440;
    --ink:#4a4a4a;
    --ink-soft:#5c5c5c;
    --paper:#ffffff;
    --backdrop:#dcdcdc;
    --rule:#d6d6d6;
  }
  *{box-sizing:border-box;margin:0;padding:0}
  html,body{width:1200px;height:836px;overflow:hidden;background:var(--backdrop);font-family:"Poppins",sans-serif;color:var(--ink)}
  .canvas{position:relative;width:1200px;height:836px}
  .flyer{position:absolute;top:48px;width:600px;height:778px;background:var(--paper);transform:scale(0.95);transform-origin:top left;overflow:hidden;box-shadow:0 10px 30px rgba(0,0,0,.18)}
  .flyer--back{left:20px}
  .flyer--front{left:610px}
  .abs{position:absolute}
  .photo{position:absolute}
  .brand{display:flex;flex-direction:column;align-items:center;gap:6px;text-align:center}
  .brand__mark{width:14px;height:14px;background:var(--green)}
  .brand__name{font-weight:500;font-size:24px;letter-spacing:.5px;color:var(--ink);line-height:1.1}
  .headline{font-weight:800;font-size:30px;line-height:1.08;letter-spacing:.6px;color:var(--ink);text-transform:uppercase}
  .details{position:absolute;left:267px;top:512px;width:310px;display:flex;flex-direction:column;gap:9px}
  .ticks{list-style:none;font-size:12.5px;line-height:19.5px;color:var(--ink)}
  .ticks li{display:flex;align-items:center;gap:9px}
  .ticks svg{width:13px;height:11px;flex:none}
  .samples{font-weight:600;font-size:11.5px;line-height:16px;color:var(--green)}
  .cta{font-weight:600;font-size:11.5px;line-height:16px;color:var(--ink)}
  .fineprint{font-size:8.6px;color:var(--ink-soft)}
  .lede{font-size:10.5px;line-height:16.5px;text-transform:uppercase;color:var(--ink)}
  .footer{position:absolute;left:0;right:0;top:725px;height:53px;border-top:1px solid var(--rule);display:flex;align-items:center;padding:0 38px;gap:34px;font-size:10.5px;color:var(--ink)}
  .footer__item{display:flex;align-items:center;gap:8px}
  .footer__item svg{width:13px;height:13px;flex:none}
  .dot{width:9px;height:9px;border-radius:50%;background:var(--ink);flex:none}
</style>
</head>
<body>
<main class="canvas">

  <!-- Back side -->
  <section class="flyer flyer--back">
    <div class="abs" style="left:215px;top:0;width:53px;height:186px;background:var(--green)"></div>
    <div class="photo" role="img" aria-label="Living room with wood-look flooring, walnut wardrobe and black-framed glass door" style="left:267px;top:0;width:333px;height:494px;background:linear-gradient(180deg,#bfb9b1 0%,#8c7e6f 45%,#b99572 75%,#d2ad83 100%)"></div>

    <div class="brand abs" style="left:25px;top:62px;width:160px">
      <span class="brand__mark"></span>
      <span class="brand__name">BRELTON’S</span>
    </div>

    <h1 class="headline abs" style="left:35px;top:170px">Quality<br>Flooring<br>Solutions</h1>

    <div class="photo" role="img" aria-label="Installer cutting a laminate plank" style="left:35px;top:289px;width:96px;height:95px;background:linear-gradient(160deg,#5a4a3c,#b9986f)"></div>
    <div class="photo" role="img" aria-label="Installer with flooring equipment on site" style="left:145px;top:289px;width:96px;height:95px;background:linear-gradient(160deg,#8e8f8c,#c9c3b6)"></div>
    <div class="photo" role="img" aria-label="Underfloor heating being laid before flooring" style="left:35px;top:402px;width:96px;height:95px;background:linear-gradient(180deg,#8a6d55,#b8372d)"></div>
    <div class="photo" role="img" aria-label="Hands fitting a vinyl plank" style="left:145px;top:402px;width:96px;height:95px;background:linear-gradient(160deg,#9c8f77,#d4c6a6)"></div>
    <div class="photo" role="img" aria-label="Finished kitchen and dining area with timber floor" style="left:35px;top:510px;width:206px;height:195px;background:linear-gradient(180deg,#8e8478 0%,#5a6b8f 30%,#a08d7c 60%,#c7b39a 100%)"></div>

    <div class="details">
      <ul class="ticks">
        <li><svg viewBox="0 0 13 11"><path d="M1 5.5l4 4L12 1" fill="none" stroke="var(--green)" stroke-width="2"/></svg>Quality Flooring Equipment</li>
        <li><svg viewBox="0 0 13 11"><path d="M1 5.5l4 4L12 1" fill="none" stroke="var(--green)" stroke-width="2"/></svg>Supply &amp; Installation</li>
        <li><svg viewBox="0 0 13 11"><path d="M1 5.5l4 4L12 1" fill="none" stroke="var(--green)" stroke-width="2"/></svg>High Quality Flooring</li>
        <li><svg viewBox="0 0 13 11"><path d="M1 5.5l4 4L12 1" fill="none" stroke="var(--green)" stroke-width="2"/></svg>Laminate, SPC Vinyl Planks</li>
        <li><svg viewBox="0 0 13 11"><path d="M1 5.5l4 4L12 1" fill="none" stroke="var(--green)" stroke-width="2"/></svg>Engineered Timber</li>
      </ul>
      <p class="samples">FREE samples delivered to your door to see quality<br>and colours – order only via our website.</p>
      <p class="cta">Just contact our friendly and knowledgeable<br>team today to find out more.</p>
      <p class="fineprint">All of our equipment have been approved by Australian standards.</p>
    </div>

    <footer class="footer">
      <span class="footer__item"><svg viewBox="0 0 13 13"><path d="M3 1.5l2 2.3-1.1 1.5c.7 1.6 2 2.9 3.6 3.6l1.5-1.1 2.3 2-1 2C6 11.6 1.4 7 1 2.5z" fill="var(--ink)"/></svg>1300 482 915</span>
      <span class="footer__item"><svg viewBox="0 0 13 13"><g fill="none" stroke="var(--ink)" stroke-width="1"><circle cx="6.5" cy="6.5" r="5.5"/><ellipse cx="6.5" cy="6.5" rx="2.4" ry="5.5"/><path d="M1 6.5h11M2 3.8h9M2 9.2h9"/></g></svg>www.breltonsflooringsolutions.com.au</span>
      <span class="footer__item"><span class="dot"></span>breltonssolutionsgroup</span>
    </footer>
  </section>

  <!-- Front side -->
  <section class="flyer flyer--front">
    <div class="photo" role="img" aria-label="Modern kitchen and dining room with marble splashback, pendant lights and light oak flooring" style="left:0;top:0;width:600px;height:520px;background:linear-gradient(180deg,#6f6d6a 0%,#8f8a83 35%,#b08f6e 62%,#cda57c 100%)"></div>
    <div class="abs" style="left:35px;top:428px;width:187px;height:270px;background:var(--green)"></div>

    <div class="brand abs" style="left:390px;top:440px;width:155px">
      <span class="brand__mark"></span>
      <span class="brand__name">BRELTON’S</span>
    </div>

    <h1 class="headline abs" style="left:265px;top:546px;font-size:29px">Quality<br>Flooring<br>Solutions</h1>
    <p class="lede abs" style="left:265px;top:652px">Supply &amp; installation of high quality<br>flooring (laminate, SPC vinyl planks<br>and engineered timber)</p>

    <footer class="footer">
      <span class="footer__item"><svg viewBox="0 0 13 13"><path d="M3 1.5l2 2.3-1.1 1.5c.7 1.6 2 2.9 3.6 3.6l1.5-1.1 2.3 2-1 2C6 11.6 1.4 7 1 2.5z" fill="var(--ink)"/></svg>1300 482 915</span>
      <span class="footer__item"><svg viewBox="0 0 13 13"><g fill="none" stroke="var(--ink)" stroke-width="1"><circle cx="6.5" cy="6.5" r="5.5"/><ellipse cx="6.5" cy="6.5" rx="2.4" ry="5.5"/><path d="M1 6.5h11M2 3.8h9M2 9.2h9"/></g></svg>www.breltonsflooringsolutions.com.au</span>
      <span class="footer__item"><span class="dot"></span>breltonssolutionsgroup</span>
    </footer>
  </section>

</main>
</body>
</html>
```